VELT MIXER FOR YOUNG BUSINESS PROFESSIONALS

Fresh, Upscale, Classy and Modern. I need some flyer designs for a business mixer coming up for young business professionals. We are targeting business owners and professionals under 40 and we will strive to bridge the gap between successful business owners and young entrepreneurs through hosting striking mixers throughout the year. The flyer needs to have simplicity but at the same time could be abstract or balanced with some complexity or is open to ideas. The event will be hosted at an art gallery. I need something unique and different and good taste but yet creative. Anyone that ends up doing a good job will be rewarded with work for the rest of the year for all of our events. I am open to the usage of colors as long as it looks striking at the end of the day. We can also keep in mind that this flyer can be the jumpstart of a series of different other flyers with variations.
Target Market(s)
Young Business Owners and Professionals under 40
Industry/Entity Type
Events
Requirements
Must have
- Must have space to put who what where when and a spot for a brief catchy title and introduction to possible guest speakers. Must keep in mind that the theme is leadership. The location is TRILK art gallery in Edmonton. Must be able to create a feeling of admiration and inspiration
Nice to have
- nice to have designer that understands and able to balance the designs to make it work. Nice to have something that is completely unique, different and striking but again following the fresh, upscale, classy and modern look.
Should not have
- should not have anything that is typical

```html
<!DOCTYPE html>
<html lang="en">
<head>
<meta charset="utf-8">
<title>VELT Business Mixer</title>
<link rel="stylesheet" href="https://fonts.googleapis.com/css2?family=Cinzel:wght@400;500&family=Josefin+Sans:wght@300;400&display=swap">
<style>
  :root {
    --ink: #0b0b0b;
    --paper: #ffffff;
    --signal: #f7e814;
    --hatch: #9a9a9a;
  }
  html, body {
    margin: 0;
    padding: 0;
    overflow: hidden;
    background: var(--paper);
  }
  .flyer {
    position: relative;
    width: 849px;
    height: 1200px;
    overflow: hidden;
    background: var(--paper);
    font-family: "Josefin Sans", sans-serif;
    color: var(--ink);
  }
  .flyer__shapes,
  .flyer__hatch {
    position: absolute;
    left: 0;
    top: 0;
  }
  .title {
    position: absolute;
    top: 62px;
    left: 34px;
    width: 815px;
    text-align: center;
    color: var(--paper);
  }
  .title__name {
    font-family: "Cinzel", serif;
    font-weight: 500;
    font-size: 112px;
    line-height: 1;
    letter-spacing: 4px;
    margin: 0;
  }
  .title__sub {
    font-family: "Josefin Sans", sans-serif;
    font-weight: 400;
    font-size: 44px;
    line-height: 1;
    margin: 10px 0 0;
  }
  .info {
    position: absolute;
    margin: 0;
  }
  .info__label {
    font-family: "Josefin Sans", sans-serif;
    font-weight: 400;
    font-size: 39px;
    line-height: 1;
    margin: 0 0 8px;
    text-transform: uppercase;
  }
  .info__line {
    font-weight: 300;
    font-size: 22px;
    line-height: 31px;
    margin: 0;
  }
  .info--right .info__line {
    line-height: 44px;
  }
  .info--right {
    right: 104px;
    text-align: right;
  }
  .info--speakers { left: 62px; top: 350px; }
  .info--time { left: 62px; top: 535px; }
  .info--attn { top: 440px; }
  .info--location { top: 655px; }
  .info--date { top: 778px; }
  .brand {
    position: absolute;
    left: 34px;
    top: 990px;
    width: 716px;
    text-align: center;
    font-family: "Cinzel", serif;
    font-weight: 400;
    font-size: 150px;
    line-height: 1.1;
    letter-spacing: 2px;
    color: var(--ink);
    margin: 0;
  }
</style>
</head>
<body>
<main class="flyer">
  <svg class="flyer__shapes" width="849" height="1200" viewBox="0 0 849 1200" aria-hidden="true">
    <rect class="field-dark" x="51" y="0" width="798" height="950" fill="var(--ink)"/>
    <polygon class="wedge-yellow" points="51,275 540,275 51,935" fill="var(--signal)"/>
    <polygon class="wedge-white" points="849,170 849,925 127,925" fill="var(--paper)"/>
    <rect class="rule-yellow" x="756" y="0" width="7" height="1200" fill="var(--signal)"/>
  </svg>
  <svg class="flyer__hatch" width="849" height="1200" role="img" aria-label="Diagonal stripe pattern in the lower left corner">
    <rect x="0" y="565" width="51" height="385" fill="var(--hatch)"/>
    <polygon points="51,700 51,935 150,935" fill="var(--hatch)"/>
  </svg>

  <header class="title">
    <h1 class="title__name">VELT</h1>
    <p class="title__sub">Business Mixer</p>
  </header>

  <section class="info info--speakers">
    <h2 class="info__label">Speakers</h2>
    <p class="info__line">NAME</p>
    <p class="info__line">Introduction</p>
    <p class="info__line">Subject</p>
    <p class="info__line">Specialty</p>
  </section>

  <section class="info info--time">
    <h2 class="info__label">Time</h2>
    <p class="info__line">7-9 PM</p>
  </section>

  <section class="info info--right info--attn">
    <h2 class="info__label">Attn</h2>
    <p class="info__line">Leaders</p>
    <p class="info__line">Business Owners</p>
    <p class="info__line">Young Business Professionals</p>
  </section>

  <section class="info info--right info--location">
    <h2 class="info__label">Location</h2>
    <p class="info__line">TRILK Art Gallery, Edmonton</p>
  </section>

  <section class="info info--right info--date">
    <h2 class="info__label">Date</h2>
    <p class="info__line">Month 15, 2015</p>
  </section>

  <p class="brand">KESTRA</p>
</main>
</body>
</html>
```